Indianapolis based store looking for a multi-page website, to include ecommerce. We sell Heron mattresses, which are manufactured in Fort Wayne, Indiana. The design line of mattresses includes the blue heron (value), white heron (mid-value) and grey heron (high end). We also offer mattresses for RV, futon and pet mattresses. We want a user-friendly website with e-commerce capability. Web pages should include pictures of our product, bio/history of operator/Heron cooperation, detailed description of the product, shopping cart. Paysend, major credit cards accepted.

Facts about the store: 4627 N. Calloway Rd Suite 210 Indianapolis, IN 46291 #317-542-7186. Domain name we would like is www.pillowharbor.com. If this domain is already taken, we would like www.pillowharbor.net. Features that set Pillow Harbor apart from competitors: local delivery within a day, product stored on site and available to take home the same day, vacuumed sealed boxed option for same day take home, dual-sided mattress options (firm/plush), locally owned/operated, locally manufactured (Fort Wayne, IN), FoamSafe-NA certified (info link for FoamSafe https://foamsafe-example.us/ )

Here is the website we will be using for background information/pictures. Please check out the descriptions/pictures for ideas. We are waiting to hear back from Heron's owners in regard to permission using their actual photos.

https://www.heronbedding-example.com/products/mattresses/

https://www.heronbedding-example.com/products/futons/

We will be attaching a price list. We will probably have more products/info to add. We are also attaching our logo which was designed with Brandly Hub but we need to get a higher res copy from the designer.

We also would like an email associated with the website/company: info@pillowharbor.com ( we are not sure how an email gets set up)

Target Market(s)

mattress shoppers!

Industry/Entity Type

Retail

Coding

Coded - Design and coding required

Number of Pages Required

5+ page

Font styles to use
Sans Serif

Colors
0455a3
cfdeed
eaf1f7

Requirements
Must have
• e-commerce/shopping cart, pictures (pets in beds, RVs, futons etc - please see websites listed in project description), watermark, user friendly, product information (please see web site listed in project description), crisp pictures/lines, should emote a sense of comfort, ability to be viewed on mobile device
• link to follow on FB/IG https://www.facebook.com/pillowharbor/ IG: pillowharbor
• ability for the customer/viewer to "contact us now/ask questions". Ability for customers to leave reviews on products/star rating
• prices should be listed next to product, not "see price in cart", ability to "sort" by price low-high, filter options (i.e. type: pet, RV, futon, mattress,) then a filter option for mattress size (twin, full, queen, king)
Should not have
• rollover/mouse over

```html
<!DOCTYPE html>
<html lang="en">
<head>
<meta charset="utf-8">
<title>Pillow Harbor — The Better Mattress</title>
<link href="https://fonts.googleapis.com/css2?family=Poppins:wght@400;500;600;700&display=swap" rel="stylesheet">
<style>
:root{
  --navy:#0d3553;
  --ink:#222831;
  --body:#4a4f55;
  --muted:#8a8f94;
  --blue:#0455a3;
  --blue-soft:#cfdeed;
  --blue-pale:#eaf1f7;
  --line:#e3e6e9;
  --white:#ffffff;
  --sale:#e4573d;
}
*{box-sizing:border-box;margin:0;padding:0}
html,body{width:1200px;height:3956px;overflow:hidden;background:var(--white)}
body{font-family:"Poppins",sans-serif;color:var(--body);font-size:13px}
.page{position:relative;width:1200px;height:3956px;overflow:hidden}
.abs{position:absolute}
.btn{position:absolute;display:flex;align-items:center;justify-content:center;background:var(--blue);color:var(--white);font-weight:600;font-size:13px;border-radius:3px}
.section-title{position:absolute;left:0;width:1200px;text-align:center;color:var(--navy);font-size:24px;font-weight:500}
.section-title::after{content:"";display:block;width:56px;height:2px;background:var(--blue);margin:16px auto 0}
.round-arrow{position:absolute;width:26px;height:26px;border-radius:50%;background:var(--ink);display:flex;align-items:center;justify-content:center}
.plain-arrow{position:absolute;width:24px;height:24px}

/* header */
.site-header{position:absolute;left:0;top:0;width:1200px;height:116px;background:var(--white)}
.brand{position:absolute;left:79px;top:38px;display:flex;align-items:center;gap:10px;font-size:24px;font-weight:600;color:var(--ink);letter-spacing:1px}
.brand-mark{width:14px;height:14px;background:var(--blue)}
.main-nav{position:absolute;left:324px;top:46px;display:flex;gap:34px;font-size:13px;color:var(--ink);font-weight:500}
.main-nav .active{color:var(--blue)}
.header-tools{position:absolute;left:1000px;top:42px;display:flex;gap:22px}

/* hero */
.hero{position:absolute;left:0;top:116px;width:1200px;height:480px;background:linear-gradient(90deg,#3b3027 0%,#4e4034 28%,#7d6d5d 42%,#d9d4ca 55%,#f3f0ea 68%,#e6e1d6 85%,#9ea56a 96%,#7b8a4a 100%)}
.hero-title{position:absolute;left:190px;width:400px;text-align:center;color:var(--white)}
.hero .t1{top:150px;font-size:30px;font-weight:600}
.hero .t2{top:182px;font-size:54px;font-weight:600;color:var(--blue-soft);letter-spacing:1px}
.hero .t3{top:258px;font-size:13px;font-weight:500}

/* collections */
.collection{position:absolute;top:750px;width:200px;text-align:center}
.collection .mark{width:84px;height:84px;margin:0 auto;border-radius:50%}
.collection .name{margin-top:36px;font-size:14px;color:var(--ink);letter-spacing:1px}

/* about */
.about-title{position:absolute;left:79px;top:1038px;color:var(--navy);font-size:22px;font-weight:500}
.about-title::after{content:"";display:block;width:120px;height:2px;background:var(--blue);margin-top:14px}
.about-copy{position:absolute;left:158px;top:1100px;width:430px;font-size:13px;line-height:24px}
.about-copy p+p{margin-top:16px}

/* products */
.product{position:absolute;top:1537px;width:322px;height:493px;background:var(--white)}
.product.featured{box-shadow:0 3px 16px rgba(4,85,163,.18)}
.product .photo{width:322px;height:322px}
.product .info{padding:18px 18px 0}
.product h3{font-size:15px;font-weight:600;color:var(--ink)}
.product.featured h3{color:var(--blue)}
.product .sub{font-size:11px;color:var(--ink);margin-top:2px}
.product .price{margin-top:12px;font-size:15px;color:var(--ink)}
.product .price s{font-size:12px;color:var(--muted);margin-left:6px}
.product .rule{height:1px;background:var(--line);margin-top:12px}
.product .meta{display:flex;align-items:center;margin-top:12px;font-size:11px;color:var(--muted);height:26px}
.product .stars{color:#b7bcc1;letter-spacing:2px;font-size:14px;margin-right:6px}
.product .actions{margin-left:auto;display:flex;gap:16px}
.sale-badge{position:absolute;left:18px;top:16px;width:48px;height:26px;border-radius:13px;background:var(--sale);color:var(--white);font-size:12px;display:flex;align-items:center;justify-content:center}

/* offer */
.offer-kicker{position:absolute;left:664px;top:2212px;font-size:26px;color:var(--navy);font-weight:500}
.offer-big{position:absolute;left:664px;top:2250px;font-size:70px;font-weight:600;color:var(--blue);letter-spacing:1px}
.offer-copy{position:absolute;left:664px;top:2356px;width:440px;font-size:13px;line-height:22px;color:var(--ink)}

/* testimonials */
.person{position:absolute;left:205px;top:2826px;width:160px;text-align:center}
.person .avatar{width:80px;height:80px;border-radius:50%;margin:0 auto;background:linear-gradient(#d8d4cf,#6f6760)}
.person .stars{margin-top:12px;color:var(--blue);font-size:18px;letter-spacing:4px}
.person .name{font-size:20px;font-weight:600;color:var(--navy);margin-top:2px}
.person .role{font-size:13px;color:var(--ink)}
.quote-box{position:absolute;left:435px;top:2835px;width:559px;height:158px;box-shadow:0 2px 14px rgba(0,0,0,.14);text-align:center;padding:22px 40px 0}
.quote-box .mark{font-size:30px;font-weight:700;color:var(--ink);line-height:28px}
.quote-box p{font-size:13px;line-height:22px;color:var(--ink);margin-top:6px}

/* news */
.news{position:absolute;top:3180px;width:238px;height:327px}
.news.featured{box-shadow:0 3px 16px rgba(4,85,163,.18)}
.news .photo{height:161px}
.news .body{padding:14px 8px 0}
.news h3{font-size:19px;font-weight:500;color:var(--ink)}
.news.featured h3{color:var(--blue)}
.news .meta{display:flex;gap:14px;font-size:10px;color:var(--muted);margin-top:6px;align-items:center}
.news .meta span{display:flex;align-items:center;gap:5px}
.news .meta i{display:inline-block;width:10px;height:9px;border:1.5px solid var(--blue)}
.news p{font-size:11px;line-height:16px;color:var(--ink);margin-top:8px}
.news .more{font-size:11px;font-weight:600;color:var(--navy);margin-top:14px}
.news.featured .more{color:var(--blue)}

/* footer */
.rule-full{position:absolute;left:79px;width:1042px;height:1px;background:#d5d9dd}
.foot-brand{position:absolute;left:79px;top:3672px;display:flex;align-items:center;gap:8px;font-size:18px;font-weight:600;color:var(--ink);letter-spacing:1px}
.foot-about{position:absolute;left:79px;top:3724px;width:330px;font-size:12px;line-height:20px;color:var(--ink)}
.socials{position:absolute;left:79px;top:3796px;display:flex;gap:26px}
.socials span{width:16px;height:16px;border-radius:3px;background:var(--ink)}
.foot-head{position:absolute;top:3672px;font-size:15px;font-weight:500;color:var(--ink);letter-spacing:1px}
.contact-line{position:absolute;left:440px;display:flex;align-items:center;gap:14px;font-size:12px;color:var(--ink)}
.contact-line b{color:var(--blue);font-size:18px;font-weight:600}
.newsletter-input{position:absolute;left:799px;top:3705px;width:200px;height:42px;border:1px solid #cfd4d8;font-size:12px;color:var(--muted);padding:0 14px;display:flex;align-items:center}
.pay{position:absolute;top:3794px;display:flex;gap:20px;left:799px}
.pay span{width:24px;height:17px;border:2px solid var(--ink);border-radius:3px}
.copyright{position:absolute;left:79px;top:3904px;font-size:11px;color:var(--ink)}
.copyright b{color:var(--blue);font-weight:500}
.foot-nav{position:absolute;right:79px;top:3904px;display:flex;gap:34px;font-size:12px;color:var(--ink)}
</style>
</head>
<body>
<div class="page">

  <header class="site-header">
    <div class="brand"><span class="brand-mark"></span>PILLOW HARBOR</div>
    <nav class="main-nav">
      <span class="active">Home</span><span>Our Story</span><span>Products</span><span>Review</span><span>Blog</span><span>Contact Us</span>
    </nav>
    <div class="header-tools">
      <svg width="18" height="18" viewBox="0 0 18 18" fill="none" stroke="#222831" stroke-width="2"><circle cx="7.5" cy="7.5" r="5.5"/><path d="M11.5 11.5L16 16"/></svg>
      <svg width="18" height="18" viewBox="0 0 24 24" fill="none" stroke="#222831" stroke-width="2.2"><path d="M12 21s-8-5.2-8-11a4.5 4.5 0 0 1 8-2.8A4.5 4.5 0 0 1 20 10c0 5.8-8 11-8 11z"/></svg>
      <svg width="20" height="18" viewBox="0 0 24 22" fill="none" stroke="#222831" stroke-width="2"><path d="M1 2h4l3 12h12l3-9H6.5"/><circle cx="9.5" cy="19" r="1.6"/><circle cx="18.5" cy="19" r="1.6"/></svg>
      <svg width="6" height="18" viewBox="0 0 6 18" fill="#222831"><circle cx="3" cy="3" r="2.2"/><circle cx="3" cy="9" r="2.2"/><circle cx="3" cy="15" r="2.2"/></svg>
    </div>
  </header>

  <section class="hero" role="img" aria-label="Bedroom photo of a quilted white mattress with two pillows on a dark wooden floor">
    <div class="hero-title t1">The Better</div>
    <div class="hero-title t2">MATTRESS</div>
    <div class="hero-title t3">For the ultimate luxury sleeping experience</div>
    <div class="btn" style="left:343px;top:322px;width:118px;height:44px;font-size:12px">SHOP NOW!</div>
    <div class="round-arrow" style="left:29px;top:224px"><svg width="10" height="10" viewBox="0 0 10 10" fill="none" stroke="#fff" stroke-width="2"><path d="M7 1L3 5l4 4"/></svg></div>
    <div class="round-arrow" style="left:1145px;top:224px"><svg width="10" height="10" viewBox="0 0 10 10" fill="none" stroke="#fff" stroke-width="2"><path d="M3 1l4 4-4 4"/></svg></div>
  </section>

  <h2 class="section-title" style="top:662px">Mattress Collections</h2>
  <div class="collection" style="left:137px"><div class="mark" role="img" aria-label="Blue heron collection emblem" style="background:#a9adb1"></div><div class="name">BLUE HERON</div></div>
  <div class="collection" style="left:501px"><div class="mark" role="img" aria-label="White heron collection emblem" style="background:#5f6a73"></div><div class="name">WHITE HERON</div></div>
  <div class="collection" style="left:855px"><div class="mark" role="img" aria-label="Grey heron collection emblem" style="background:#1b1b1b"></div><div class="name">GREY HERON</div></div>

  <h2 class="about-title">Mattress About</h2>
  <div class="about-copy">
    <p>Lorem Ipsum is simply dummy text of the printing and typesetting industry. Lorem Ipsum has been the industry's standard dummy text ever since the 1500s, when an unknown printer took a galley.</p>
    <p>scrambled it to make a type specimen book. It has survived not only five centuries, but also the leap into electronic typesetting, Ipsum.</p>
  </div>
  <div class="btn" style="left:158px;top:1311px;width:119px;height:47px">Read More</div>
  <div class="abs" role="img" aria-label="Photo of a woman unpacking a vacuum-sealed rolled mattress" style="left:752px;top:1028px;width:382px;height:330px;background:linear-gradient(160deg,#ffffff 0%,#eef0f2 30%,#d7dbde 60%,#c3c8cc 80%,#ffffff 100%)"></div>

  <h2 class="section-title" style="top:1438px">Mattress Products</h2>
  <div class="round-arrow" style="left:27px;top:1743px"><svg width="10" height="10" viewBox="0 0 10 10" fill="none" stroke="#fff" stroke-width="2"><path d="M7 1L3 5l4 4"/></svg></div>
  <div class="round-arrow" style="left:1146px;top:1743px"><svg width="10" height="10" viewBox="0 0 10 10" fill="none" stroke="#fff" stroke-width="2"><path d="M3 1l4 4-4 4"/></svg></div>

  <article class="product" style="left:79px">
    <div class="photo" role="img" aria-label="Blue heron mattress on a black bed frame in a bright room" style="background:linear-gradient(180deg,#f4ecdd 0%,#ede1c9 45%,#dcdcdc 62%,#4a4a4a 74%,#cdb48e 80%,#b8996c 100%)"></div>
    <div class="info">
      <h3>Blue Heron Collection</h3>
      <div class="sub">A Penny For Your Dreams</div>
      <div class="price">$184.00<s>$230.00</s></div>
      <div class="rule"></div>
      <div class="meta"><span class="stars">☆☆☆☆☆</span>(0 Review)
        <span class="actions">
          <svg width="14" height="14" viewBox="0 0 24 24" fill="none" stroke="#222831" stroke-width="2.4"><path d="M12 21s-8-5.2-8-11a4.5 4.5 0 0 1 8-2.8A4.5 4.5 0 0 1 20 10c0 5.8-8 11-8 11z"/></svg>
          <svg width="14" height="14" viewBox="0 0 14 14" fill="none" stroke="#222831" stroke-width="1.8"><path d="M2 12L12 2M8 2h4v4M6 12H2V8"/></svg>
        </span>
      </div>
    </div>
  </article>

  <article class="product featured" style="left:440px">
    <div class="photo" role="img" aria-label="White heron mattress on a dark frame against a stone wall" style="background:linear-gradient(180deg,#c9bba8 0%,#b7a690 45%,#e6e6e6 60%,#2a2a2a 74%,#a8916f 82%,#8d7657 100%)"></div>
    <div class="info">
      <h3>White Heron Collection</h3>
      <div class="sub">Value You Will Feel All Night Long!</div>
      <div class="price">$124.00<s>$230.00</s></div>
      <div class="rule"></div>
      <div class="meta"><span class="btn" style="position:static;width:118px;height:34px;font-size:12px">BUY NOW!</span>
        <span class="actions">
          <svg width="14" height="14" viewBox="0 0 24 24" fill="none" stroke="#222831" stroke-width="2.4"><path d="M12 21s-8-5.2-8-11a4.5 4.5 0 0 1 8-2.8A4.5 4.5 0 0 1 20 10c0 5.8-8 11-8 11z"/></svg>
          <svg width="14" height="14" viewBox="0 0 14 14" fill="none" stroke="#222831" stroke-width="1.8"><path d="M2 12L12 2M8 2h4v4M6 12H2V8"/></svg>
        </span>
      </div>
    </div>
  </article>

  <article class="product" style="left:802px">
    <div class="photo" role="img" aria-label="Grey heron mattress on a dark frame in an attic room" style="background:linear-gradient(180deg,#b9ac9c 0%,#a39481 45%,#6f7376 60%,#2a2a2a 74%,#a48560 82%,#8a6c4a 100%)"></div>
    <span class="sale-badge">-20%</span>
    <div class="info">
      <h3>Grey Heron Collection</h3>
      <div class="sub">Comfort You Can Feel With Your Eyes Closed!</div>
      <div class="price">$134.00<s>$230.00</s></div>
      <div class="rule"></div>
      <div class="meta"><span class="stars">☆☆☆☆☆</span>(0 Review)
        <span class="actions">
          <svg width="14" height="14" viewBox="0 0 24 24" fill="none" stroke="#222831" stroke-width="2.4"><path d="M12 21s-8-5.2-8-11a4.5 4.5 0 0 1 8-2.8A4.5 4.5 0 0 1 20 10c0 5.8-8 11-8 11z"/></svg>
          <svg width="14" height="14" viewBox="0 0 14 14" fill="none" stroke="#222831" stroke-width="1.8"><path d="M2 12L12 2M8 2h4v4M6 12H2V8"/></svg>
        </span>
      </div>
    </div>
  </article>

  <div class="abs" role="img" aria-label="Woman meditating in a yoga pose beside a potted plant" style="left:145px;top:2123px;width:488px;height:400px;background:radial-gradient(ellipse at 55% 60%,#9fd3d8 0%,#c9d7da 22%,#eef2f3 48%,#ffffff 72%)"></div>
  <div class="abs" role="img" aria-label="Thick foam mattress with a kraft-colored side panel" style="left:79px;top:2492px;width:1042px;height:145px;background:linear-gradient(180deg,#f3e7c9 0%,#eedcb4 36%,#c89e6c 40%,#b8895a 100%)"></div>
  <div class="offer-kicker">Special Offers</div>
  <div class="offer-big">GET 30% OFF</div>
  <p class="offer-copy">Lorem Ipsum is simply dummy text of the printing and typesetting industry. Lorem Ipsum has been the industry's standard text a galley.</p>
  <div class="btn" style="left:664px;top:2436px;width:122px;height:48px">Read More</div>

  <h2 class="section-title" style="top:2727px">Testimonials</h2>
  <svg class="plain-arrow" style="left:154px;top:2899px" viewBox="0 0 24 24" fill="none" stroke="#222831" stroke-width="2.4"><path d="M15 5l-7 7 7 7"/></svg>
  <svg class="plain-arrow" style="left:1022px;top:2899px" viewBox="0 0 24 24" fill="none" stroke="#222831" stroke-width="2.4"><path d="M9 5l7 7-7 7"/></svg>
  <div class="person">
    <div class="avatar" role="img" aria-label="Customer portrait"></div>
    <div class="stars">★★★★★</div>
    <div class="name">Dana Merrow</div>
    <div class="role">Manager</div>
  </div>
  <div class="quote-box">
    <div class="mark">“</div>
    <p>"Lorem ipsum dolor sit amet, consectetur adipiscing elit, sed do eiusmod tempor incididunt ut labore et dolore magna aliqua. Ut enim ad minim commodo consequat.</p>
  </div>

  <h2 class="section-title" style="top:3078px">Latest News</h2>
  <svg class="plain-arrow" style="left:25px;top:3330px" viewBox="0 0 24 24" fill="none" stroke="#222831" stroke-width="2.4"><path d="M15 5l-7 7 7 7"/></svg>
  <svg class="plain-arrow" style="left:1148px;top:3330px" viewBox="0 0 24 24" fill="none" stroke="#222831" stroke-width="2.4"><path d="M9 5l7 7-7 7"/></svg>

  <article class="news" style="left:79px">
    <div class="photo" role="img" aria-label="Platform bed with a dark red cover in a warm room" style="background:linear-gradient(180deg,#d9cbb8 0%,#c2ad93 35%,#7a3a2a 55%,#5a2a20 100%)"></div>
    <div class="body"><h3>Platform Sets</h3>
      <div class="meta"><span><i></i>October 18,2017</span><span><i></i>comment</span></div>
      <p>Duis aute irure dolor in reprehenderit in voluptate velit esse cillum dolore eu fugiat nulla pariatur.</p>
      <div class="more">Read more</div></div>
  </article>
  <article class="news featured" style="left:345px">
    <div class="photo" role="img" aria-label="Travel trailer parked among orange autumn trees" style="background:linear-gradient(180deg,#e39a3c 0%,#c96d22 40%,#d9d9d6 62%,#9a7a52 80%,#6d8a3c 100%)"></div>
    <div class="body"><h3>Sweet RV's</h3>
      <div class="meta"><span><i></i>October 18,2017</span><span><i></i>comment</span></div>
      <p>Duis aute irure dolor in reprehenderit in voluptate velit esse cillum dolore eu fugiat nulla pariatur.</p>
      <div class="more">Read more</div></div>
  </article>
  <article class="news" style="left:614px">
    <div class="photo" role="img" aria-label="Mattress on a dark platform against a green wall" style="background:linear-gradient(180deg,#86c03c 0%,#9cc65a 45%,#dfe2e4 62%,#2e3033 78%,#bfb8ad 100%)"></div>
    <div class="body"><h3>Platform Sets</h3>
      <div class="meta"><span><i></i>October 18,2017</span><span><i></i>comment</span></div>
      <p>Duis aute irure dolor in reprehenderit in voluptate velit esse cillum dolore eu fugiat nulla pariatur.</p>
      <div class="more">Read more</div></div>
  </article>
  <article class="news" style="left:883px">
    <div class="photo" role="img" aria-label="Spring mattress on a wooden bed frame" style="background:linear-gradient(180deg,#6a4a35 0%,#8a6a50 35%,#e8e4de 55%,#5a3c2a 75%,#c9b9a6 100%)"></div>
    <div class="body"><h3>Spring Mattress</h3>
      <div class="meta"><span><i></i>October 18,2017</span><span><i></i>comment</span></div>
      <p>Duis aute irure dolor in reprehenderit in voluptate velit esse cillum dolore eu fugiat nulla pariatur.</p>
      <div class="more">Read more</div></div>
  </article>

  <div class="rule-full" style="top:3594px"></div>

  <footer>
    <div class="foot-brand"><span class="brand-mark" style="width:11px;height:11px"></span>PILLOW HARBOR</div>
    <p class="foot-about">Lorem ipsum dolor sit amet, consectetur adipiscing elit, sed do eiusmod tempor incididunt ut labore consequat.</p>
    <div class="socials" aria-label="Social links"><span></span><span></span><span></span><span></span></div>

    <div class="foot-head" style="left:440px">CONTACT US</div>
    <div class="contact-line" style="top:3714px">
      <svg width="14" height="16" viewBox="0 0 14 18" fill="none" stroke="#222831" stroke-width="1.8"><path d="M7 17s-5.5-6-5.5-10a5.5 5.5 0 0 1 11 0C12.5 11 7 17 7 17z"/><circle cx="7" cy="7" r="2"/></svg>
      P.O. Harbor Plaza 4627 Calloway IN 46291</div>
    <div class="contact-line" style="top:3750px">
      <svg width="14" height="14" viewBox="0 0 16 16" fill="#222831"><path d="M3.5 1l2.5 3-1.5 2a9 9 0 0 0 5 5l2-1.5 3 2.5-1.5 2.5C7 15 1 9 1 2.5z"/></svg>
      Call Us : - <b>888.410.2273</b></div>
    <div class="contact-line" style="top:3794px">
      <svg width="15" height="12" viewBox="0 0 16 12" fill="none" stroke="#222831" stroke-width="1.6"><rect x="1" y="1" width="14" height="10"/><path d="M1 1l7 6 7-6"/></svg>
      contact@example.com</div>

    <div class="foot-head" style="left:799px">GET NEWSLETTER</div>
    <div class="newsletter-input">Your email Address</div>
    <div class="btn" style="left:1007px;top:3705px;width:114px;height:42px;font-size:11px">SUBSCRIBE</div>
    <div class="pay" aria-label="Accepted payment methods"><span></span><span></span><span></span><span></span></div>
  </footer>

  <div class="rule-full" style="top:3876px"></div>
  <div class="copyright">Copyright © 2018 <b>pillowharbor</b>. All rights reserved</div>
  <nav class="foot-nav"><span>Our Story</span><span>Products</span><span>Review</span><span>Blog</span><span>Contact Us</span></nav>

</div>
</body>
</html>
```